Luxury Business Card Design for High-End Window Treatments

Gilded Vantages
Custom Plantation Shutters & Architectural Shading Systems

⸻

BACK

Daniel Forsythe
Owner

Custom Interior & Exterior Window Treatments

919-482-7034
gildedvantages.com

I have included a picture that I’m hoping we can use on the back, but I’m also wondering if you can get rid of the ladder? Should we get rid of shutters , shades and blinds underneath Gilded Vantages?

Target Market(s)

High-end residential homeowners, custom home builders, architects, interior designers, and luxury renovation clients seeking premium plantation shutters and motorized architectural shading systems.

Industry/Entity Type

Custom Window treatments

Contact Information for Business Card

Front Gilded Vantages Custom Plantation Shutters Motorized Architectural Shading Systems BACK Daniel Forsythe Owner 919-482-7034 GildedVantages.com Custom Interior & Exterior Window Treatments By Appointment

Requirements
Nice to have
• Not 100% sure on nice to halves or the color but you can definitely check out my website to get a better understanding of what I’m trying to do

```html
<!DOCTYPE html>
<html lang="en">
<head>
<meta charset="utf-8">
<title>Gilded Vantages — Business Card</title>
<link rel="stylesheet" href="https://fonts.googleapis.com/css2?family=Cormorant+Garamond:ital,wght@0,400;0,500;0,600;1,400;1,500&display=swap">
<style>
  :root {
    --backdrop: #1a1f2b;
    --card: #1f1f22;
    --card-edge: #2a2a2e;
    --gold: #d9c08f;
    --gold-line: #8f7b55;
    --ivory: #ece6da;
    --ivory-soft: #d8d2c6;
    --divider: #6d6a66;
    --dusk-sky: #5d6f86;
    --dusk-house: #3b3f46;
    --dusk-ground: #2b2f28;
  }
  * { box-sizing: border-box; margin: 0; padding: 0; }
  html, body {
    width: 1200px; height: 770px; overflow: hidden;
    background: var(--backdrop);
    font-family: "Cormorant Garamond", Georgia, serif;
  }
  .sheet {
    width: 1200px; height: 770px;
    display: flex; align-items: center; justify-content: center; gap: 40px;
  }
  .card {
    position: relative;
    width: 540px; height: 310px;
    border-radius: 16px;
    background: linear-gradient(160deg, var(--card-edge), var(--card) 55%);
    overflow: hidden;
    box-shadow: 0 10px 30px rgba(0,0,0,.45);
  }

  /* Front */
  .card-front { text-align: center; }
  .brand-name {
    position: absolute; left: 0; right: 0; top: 44px;
    color: var(--gold);
    font-weight: 400; font-size: 60px; line-height: 58px;
  }
  .brand-divider {
    position: absolute; left: 110px; top: 200px;
    width: 320px; height: 1px;
    background: var(--gold-line);
  }
  .front-tagline {
    position: absolute; left: 0; right: 0; top: 218px;
    color: var(--ivory); font-weight: 500;
    font-size: 21px; line-height: 28px; letter-spacing: .3px;
  }

  /* Back */
  .porch-photo {
    position: absolute; left: 0; top: 0; width: 360px; height: 310px;
    background: linear-gradient(180deg, var(--dusk-sky) 0%, var(--dusk-house) 32%, #4a4538 58%, var(--dusk-ground) 100%);
    -webkit-mask-image: linear-gradient(90deg, #000 50%, transparent 88%);
    mask-image: linear-gradient(90deg, #000 50%, transparent 88%);
  }
  .contact {
    position: absolute; left: 300px; top: 26px; right: 16px;
    color: var(--ivory);
  }
  .contact-name { font-size: 27px; font-weight: 600; line-height: 32px; }
  .contact-role { font-style: italic; font-size: 18px; color: var(--ivory-soft); line-height: 22px; }
  .contact-services { margin-top: 20px; font-size: 19px; font-weight: 500; line-height: 24px; }
  .contact-rule { margin: 14px 0 12px; height: 1px; background: var(--divider); width: 190px; }
  .contact-line { display: flex; align-items: center; gap: 10px; font-weight: 500; }
  .contact-line svg { flex: none; }
  .contact-phone { font-size: 22px; line-height: 30px; }
  .contact-web { font-size: 20px; line-height: 30px; margin-top: 4px; }
  .contact-note { margin-top: 10px; font-style: italic; font-size: 18px; color: var(--ivory-soft); }
</style>
</head>
<body>
<main class="sheet">
  <section class="card card-front" aria-label="Card front">
    <h1 class="brand-name">Gilded<br>Vantages</h1>
    <div class="brand-divider" aria-hidden="true"></div>
    <p class="front-tagline">Custom Plantation Shutters<br>Motorized Architectural Shading Systems</p>
  </section>

  <section class="card card-back" aria-label="Card back">
    <div class="porch-photo" role="img" aria-label="Photograph of a white-columned home porch at dusk with lit windows and two Adirondack chairs"></div>
    <div class="contact">
      <h2 class="contact-name">Daniel Forsythe</h2>
      <p class="contact-role">Owner</p>
      <p class="contact-services">Custom Interior &amp; Exterior<br>Window Treatments</p>
      <div class="contact-rule"></div>
      <p class="contact-line contact-phone">
        <svg width="18" height="18" viewBox="0 0 24 24" aria-hidden="true"><path fill="var(--ivory)" d="M6.6 10.8a15.1 15.1 0 0 0 6.6 6.6l2.2-2.2a1 1 0 0 1 1-.25 11.4 11.4 0 0 0 3.6.57 1 1 0 0 1 1 1V20a1 1 0 0 1-1 1A17 17 0 0 1 3 4a1 1 0 0 1 1-1h3.5a1 1 0 0 1 1 1c0 1.25.2 2.45.57 3.57a1 1 0 0 1-.25 1z"/></svg>
        919-482-7034
      </p>
      <p class="contact-line contact-web">
        <svg width="18" height="18" viewBox="0 0 24 24" aria-hidden="true" fill="none" stroke="var(--ivory)" stroke-width="1.6"><circle cx="12" cy="12" r="9.5"/><ellipse cx="12" cy="12" rx="4.2" ry="9.5"/><line x1="2.5" y1="12" x2="21.5" y2="12"/><path d="M4.5 7h15M4.5 17h15"/></svg>
        gildedvantages.com
      </p>
      <p class="contact-note">By Appointment</p>
    </div>
  </section>
</main>
</body>
</html>
```